Velmora Lux Hair Extension Box Design and inside care instructional card/booklet (sample provided)

https://www.filecrate-share.com/sh/qk7rm2pz9lwbx4c/ZaP3tyHnmu is a link to dropbox pictures
am looking for a creative box design. I think it would be nice if the box looked like a highend fashion ad but wrapped around a box. The file must be high resolution so the print work does not look faded which is a critique of my current box attached.
I like the background color to be all black or all white.
I usually am drawn toward Emerald Green and Eggplant colors but I also like clean cut colors like white, gold, or gun metal grey or platinums.
I am open to creative designers thoughts on what looks best. No matter what think HIGH HIGH END.
On the inside we will provide a small (matching) instructional care card tagged to the hair.
Reason: I want to send feedback to current designers and give them adequate time to make changes.
I want to see multiple ethicities on the box.
ALL designers can you take my current box and update the pictures on the front, make it a high vector file, and change the information on the back. Lastly please include the maintenance card.
Target Market(s)
It is for all but I want anyone who holds it to feel like it is the most HIGH END hair and skincare line.
https://www.filecrate-share.com/sh/qk7rm2pz9lwbx4c/ZaP3tyHnmu
Industry/Entity Type
Fashion
Logo Text
Velmora Lux
Requirements
Must have
- 1. High Resolution Vector File
2. Must be able to print with sharp image
3. The box needs to look like a no other on the market. I want the packaging to look expensive compared to most.
4. Please be create (I think I want my box to resemble a high end ad wrapped around a box)
5. website on the box:
www.shopvelmoralux.com
6. I would like to see social media on the box too (but only if it looks good)
Chatterfeed @VelmoraLux
Peepline @VelmoraLux
VelmoraLux.Brevlog.com
7. Inside panel of box (currently all white needs to have one of the logos staggered on the inside pls) or some awesome image like a coupon code or advertisement.
Back Panel of box
Our hair is 100% Remy Human Hair
Our hair comes in Hand Sewn Double Drawn, Hand Sewn Single Drawn, Machine Sewn Double Drawn, Machine Sewn Single Drawn
We provide clip-ins, tape weft, loose strand or braiding hair and weft hair extension. Add faux eye lashes to your look to complete your style.
Information on inside instructional Care Card:
Velmora Lux Hair Care Recommendations Manual
Hair extensions must receive proper care to ensure maximum performance.
Washing
1. Wash hair Weekly or Biweekly.
Brush your hair in a downward motion starting at the ends and working your way toward the weft. Remove all tangles before washing it.
Remember that too much of any dirt, sweat, or over use of products can cause the hair to be less manageable.
2. Use moisturizing hair care products like conditioner to keep it soft.
Do not overly condition as it can weigh the hair down. We recommend a nickel size amount for shorter lengths and a quarter size amount for longer lengths.
This step is especially important if you are using clip in hair extensions because the hair will not get any of the moisture from the natural oils your scalp produces.
If you deep condition once a week be sure to rinse thoroughly.
3. Use cool to tepid water.
Daily
1. Do not over heat.
When adding heat remember that it is human hair. And like human hair over heating can cause hair damage.
2. Use a heat protectant.
Whether it’s a blow dryer, curling iron or flat iron, they all have one thing in common: they damage your hair. If you want to make your extensions last, your best bet is to use a heat protectant whenever you use a heated appliance on your hair. This simple step will prevent breakage and keep your locks looking great a lot longer
3. If looking to add moisture and/or shine a dime size amount of moisturizing hair products or serum.
We do not recommend using Instant conditioners or heavy grease on the hair. When finishing your style use only a dime size of any product to avoid weighing the hair down.
Maintenance
1. Though some styles do not require professional treatment we recommend using professional hair care specialist when initially putting any extensions in your hair especially for the first time.
2. Seek a professional to remove extensions
3. Brushing
Use a soft bristle brush. Harsh brushes or overly brushing is not necessary. Love Your Hair! And it will love you back by being manageable, long-lasting, and versatile.
4. Keep ends trimmed. It is real hair and can get split ends. Trim .5 to 1 inch every 8 weeks.
5. Tutorial are provided on our blog at VelmoraLux.com.
Exercise
1. Gently brush hair up into a ponytail.
2. Wash all chlorine from hair after swimming and use a hair cap. Too much chlorine can decrease longevity of the hair.
Nightly
1. Part hair down the middle. Place in two French braids.
2. Wrap hair and tie with a silk scarf or Dorinda-Lee Tamsworth head wrap.
3. Make one long French braid in the back.
4. Never sleep on wet hair. It can cause hair longevity to decrease and become less pliable.
Hair Coloring
1. Professional Hair Care Specialist Only
For maximum performance use Velmora Lux Hair Care Products. Shop online at www.ShopVelmoraLux.com. Tutorials are provided on our blog at www.VelmoraLux.com.
Like us on Chatterfeed @VelmoraLux and Peepline @VelmoraLux
Join our online Soap Opera at TressSaga.brevlog.com
Copywright 2014 Velmora Lux Spa and Salon
Nice to have
- Elite, Sleek, sexy, and upmarket. The box must include the following information and you do not have to use the attached photos. I can provide others or they can be incorporated. The feedback given about the first box is that Black American clientelle did not see them reflected in the box. We like the idea of having women's images on the box but want the ethnicities to be diverse if used.
Please look at my website www.velmoralux.com to get familiar with the company style.
And proof website of new Product Boutique http://proof.quillsitebuilder-demo.com/velmoralux/
BE CREATIVE
Feel free to email me at Rosalind@velmoralux.com subject line (Sketch Pool Box)
Should not have
- Red

```html
<!DOCTYPE html>
<html lang="en">
<head>
<meta charset="utf-8">
<title>Velmora Lux Hair Care Recommendations Manual</title>
<link href="https://fonts.googleapis.com/css2?family=Open+Sans:wght@400;600;700&display=swap" rel="stylesheet">
<style>
  :root {
    --page-bg: #e6e6e8;
    --card-bg: #000000;
    --card-text: #f2f2f2;
    --logo-panel: #141414;
    --logo-text: #c9c2c6;
  }
  * { box-sizing: border-box; margin: 0; padding: 0; }
  html, body { width: 1200px; height: 900px; overflow: hidden; }
  body {
    background: var(--page-bg);
    font-family: "Open Sans", Arial, sans-serif;
    position: relative;
  }
  .care-card {
    position: absolute;
    top: 126px;
    width: 301px;
    height: 669px;
    background: var(--card-bg);
    border-radius: 26px;
    color: var(--card-text);
    font-size: 9.4px;
    line-height: 11.6px;
    text-align: justify;
  }
  .care-card--front { left: 74px; padding: 0 29px; }
  .care-card--back { left: 406px; padding: 46px 29px 0; }
  .brand-panel {
    width: 150px;
    height: 97px;
    margin: 0 auto;
    background: var(--logo-panel);
    display: flex;
    align-items: center;
    justify-content: center;
    color: var(--logo-text);
    font-size: 13px;
    font-weight: 400;
    letter-spacing: 3px;
    text-transform: uppercase;
  }
  .manual-title {
    margin: 16px 0 14px;
    text-align: center;
    font-size: 20px;
    line-height: 24px;
    font-weight: 400;
    font-variant: small-caps;
    letter-spacing: 0.3px;
  }
  .section-title {
    font-weight: 700;
    font-size: 9.6px;
    margin-top: 12px;
  }
  .care-card--back .section-title:first-child { margin-top: 0; }
  .closing { margin-top: 22px; }
  .closing + .closing { margin-top: 12px; }
  .copyright { position: absolute; left: 29px; bottom: 36px; }
</style>
</head>
<body>

<section class="care-card care-card--front">
  <div class="brand-panel">Velmora Lux</div>
  <h1 class="manual-title">Recommendations Manual</h1>
  <p>Hair extensions must receive proper care to ensure maximum performance.</p>

  <h2 class="section-title">Washing</h2>
  <p>1. Wash hair Weekly or Biweekly.</p>
  <p>Brush your hair in a downward motion starting at the ends and working your way toward the weft. Remove all tangles before washing it.</p>
  <p>Remember that too much of any dirt, sweat, or over use of products can cause the hair to be less manageable.</p>
  <p>2. Use moisturizing hair care products like conditioner to keep it soft.</p>
  <p>Do not overly condition as it can weigh the hair down. We recommend a nickel size amount for shorter lengths and a quarter size amount for longer lengths.</p>
  <p>This step is especially important if you are using clip in hair extensions because the hair will not get any of the moisture from the natural oils your scalp produces.</p>
  <p>If you deep condition once a week be sure to rinse thoroughly.</p>
  <p>3. Use cool to tepid water.</p>

  <h2 class="section-title">Daily</h2>
  <p>1. Do not over heat.</p>
  <p>When adding heat remember that it is human hair. And like human hair over heating can cause hair damage.</p>
  <p>2. Use a heat protectant.</p>
  <p>Whether it’s a blow dryer, curling iron or flat iron, they all have one thing in common: they damage your hair. If you want to make your extensions last, your best bet is to use a heat protectant whenever you use a heated appliance on your hair. This simple step will prevent breakage and keep your locks looking great a lot longer</p>
  <p>3. If looking to add moisture and/or shine a dime size amount of moisturizing hair products or serum.</p>
  <p>We do not recommend using Instant conditioners or heavy grease on the hair. When finishing your style use only a dime size of any product to avoid weighing the hair down.</p>
</section>

<section class="care-card care-card--back">
  <h2 class="section-title">Maintenance</h2>
  <p>1. Though some styles do not require professional treatment we recommend using professional hair care specialist when initially putting any extensions in your hair especially for the first time.</p>
  <p>2. Seek a professional to remove extensions</p>
  <p>3. Brushing</p>
  <p>Use a soft bristle brush. Harsh brushes or overly brushing is not necessary. Love Your Hair! And it will love you back by being manageable, long-lasting, and versatile.</p>
  <p>4. Keep ends trimmed. It is real hair and can get split ends. Trim .5 to 1 inch every 8 weeks.</p>
  <p>5. Tutorial are provided on our blog at VelmoraLux.com.</p>

  <h2 class="section-title">Exercise</h2>
  <p>1. Gently brush hair up into a ponytail.</p>
  <p>2. Wash all chlorine from hair after swimming and use a hair cap. Too much chlorine can decrease longevity of the hair.</p>

  <h2 class="section-title">Nightly</h2>
  <p>1. Part hair down the middle. Place in two French braids.</p>
  <p>2. Wrap hair and tie with a silk scarf or Dorinda-Lee Tamsworth head wrap.</p>
  <p>3. Make one long French braid in the back.</p>
  <p>4. Never sleep on wet hair. It can cause hair longevity to decrease and become less pliable.</p>

  <h2 class="section-title">Hair Coloring</h2>
  <p>1.Professional Hair Care Specialist Only</p>

  <p class="closing">For maximum performance use Velmora Lux Hair Care Products. Shop online at www.ShopVelmoraLux.com. Tutorials are provided on our blog at www.VelmoraLux.com.</p>
  <p class="closing">Like us on Chatterfeed @VelmoraLux and Peepline @VelmoraLux<br>Join our online Soap Opera at TressSaga.brevlog.com</p>

  <p class="copyright">Copyright 2014 Velmora Lux Spa and Salon</p>
</section>

</body>
</html>
```